Clear Meadow Cleaning Services - New Brochure Design Project

Need a very good and polished Brochure from my Commercial Cleaning Services business. I have attached what I have done in the past. Need to take to the next level . Something that will compliment my website .https://quentin-v.sitenook.example/

Target Market(s)

Business /Schools/Churches/ Just about any non-residential establishment

Requirements
Must have
• Professional / Polished look and feel

```html
<!DOCTYPE html>
<html lang="en">
<head>
<meta charset="utf-8">
<title>Clear Meadow Cleaning Services – Tri-fold Brochure</title>
<link rel="stylesheet" href="https://fonts.googleapis.com/css2?family=Open+Sans:ital,wght@0,400;0,600;0,700;1,400&family=Oswald:wght@500;600&display=swap">
<style>
  :root{
    --blue:#2aa8de;
    --blue-deep:#1b8fc4;
    --green:#8dc63f;
    --green-deep:#5e9f2c;
    --ink:#4a4a4a;
    --mist:#e7e8ea;
    --page:#eef0f2;
    --white:#ffffff;
  }
  *{box-sizing:border-box;margin:0;padding:0}
  html,body{width:1200px;height:928px;overflow:hidden;background:var(--page)}
  body{font-family:"Open Sans",Arial,sans-serif;color:var(--ink);position:relative}
  .spread{position:absolute;left:20px;width:1160px;height:440px;background:var(--white);box-shadow:0 2px 8px rgba(0,0,0,.12);overflow:hidden}
  .spread--inside{top:16px}
  .spread--outside{top:472px}
  .spread > svg.backdrop{position:absolute;inset:0;width:1160px;height:440px}
  .fold{position:absolute;top:0;bottom:0;width:1px;background:rgba(0,0,0,.06)}
  .abs{position:absolute}
  .panel-title{font-weight:600;font-size:20px;letter-spacing:.5px;color:var(--white)}
  .rule{height:2px;background:var(--white);width:150px;margin-top:6px}
  .body-copy{font-size:11px;line-height:1.45;text-align:justify}
  .body-copy--light{color:var(--white)}
  .service-list{list-style:none;font-size:11px;color:var(--white);text-transform:uppercase}
  .service-list li{display:flex;align-items:center;gap:7px;margin-bottom:5px}
  .tick{width:13px;height:13px;flex:none}
  .heading-green{font-weight:700;font-size:19px;line-height:1.1;color:var(--green);text-transform:uppercase;text-align:right}
  .check-grid{display:grid;grid-template-columns:1fr 1fr;gap:4px 10px;list-style:none;font-size:10.5px;font-style:italic}
  .check-grid li{display:flex;align-items:center;gap:5px}
  .call-badge{width:80px;height:80px;border-radius:50%;background:var(--blue);border:4px solid var(--white);color:var(--white);text-align:center;font-size:8.5px;font-weight:700;display:flex;flex-direction:column;align-items:center;justify-content:center;line-height:1.25}
  .why-list{list-style:none;color:var(--white);font-size:12.5px;font-weight:600}
  .why-list li{display:flex;align-items:center;gap:9px;margin-bottom:8px;line-height:1.15}
  .why-icon{width:20px;height:20px;flex:none}
  .promise{text-align:center;font-family:"Oswald","Arial Narrow",sans-serif;text-transform:uppercase}
  .promise__cta{color:var(--green);font-size:19px;line-height:1}
  .promise__main{color:#555;font-size:19px;line-height:1.05}
  .promise__tag{font-family:"Open Sans",Arial,sans-serif;text-transform:none;font-size:15px;color:#555;line-height:1.15;margin-top:4px}
  .contact-list{list-style:none;font-size:11px}
  .contact-list li{display:flex;align-items:center;gap:10px;margin-bottom:11px;line-height:1.25}
  .contact-icon{width:18px;height:18px;flex:none}
  .brand-name{font-size:22px;font-weight:400;color:var(--green);text-align:center}
  .brand-dot{display:inline-block;width:14px;height:14px;border-radius:50%;background:var(--blue);margin-right:8px;vertical-align:middle}
  .brand-tag{font-size:15px;color:var(--green);text-align:center}
  .cover-band-title{font-weight:700;font-size:17px;color:var(--white);text-align:center;text-transform:uppercase;line-height:1.2}
  .cover-url{font-weight:700;font-size:13px;color:var(--white);text-align:center}
</style>
</head>
<body>

<section class="spread spread--inside" aria-label="Brochure inside">
  <svg class="backdrop" viewBox="0 0 1160 440" aria-hidden="true">
    <defs>
      <linearGradient id="photoInterior" x1="0" y1="0" x2="1" y2="1">
        <stop offset="0" stop-color="#f2f2ef"/><stop offset="1" stop-color="#c9cdc8"/>
      </linearGradient>
      <linearGradient id="photoWorker" x1="0" y1="0" x2="1" y2="1">
        <stop offset="0" stop-color="#eaf0f3"/><stop offset=".6" stop-color="#8fb3c7"/><stop offset="1" stop-color="#e7c24a"/>
      </linearGradient>
      <linearGradient id="photoCart" x1="0" y1="0" x2="1" y2="1">
        <stop offset="0" stop-color="#eceef0"/><stop offset=".7" stop-color="#b7bcc2"/><stop offset="1" stop-color="#e9cf3c"/>
      </linearGradient>
    </defs>
    <path d="M0 0H387V215C300 238 190 262 0 300Z" fill="var(--blue)"/>
    <path d="M0 300C190 262 300 238 387 215V232C300 252 190 278 0 318Z" fill="var(--green)"/>
    <path d="M774 0H1160V50C1050 58 900 62 774 86Z" fill="var(--blue)"/>
    <path d="M672 16C712 72 694 152 620 188" fill="none" stroke="var(--green)" stroke-width="10"/>
    <path d="M0 398C300 384 720 420 1160 360V378C720 438 300 402 0 416Z" fill="var(--blue)"/>
    <path d="M0 416C300 402 720 438 1160 378V440H0Z" fill="var(--green)"/>
    <g role="img" aria-label="Photo: cleaner in apron wiping a desk">
      <circle cx="112" cy="340" r="82" fill="var(--green)"/>
      <circle cx="112" cy="340" r="74" fill="url(#photoWorker)"/>
    </g>
    <g role="img" aria-label="Photo: bright tidy dining room interior">
      <circle cx="580" cy="84" r="80" fill="var(--green)"/>
      <circle cx="580" cy="84" r="72" fill="url(#photoInterior)"/>
    </g>
    <g role="img" aria-label="Photo: cleaning cart and wet floor sign in an office">
      <circle cx="1072" cy="334" r="70" fill="var(--blue)"/>
      <circle cx="1072" cy="334" r="63" fill="url(#photoCart)"/>
    </g>
  </svg>
  <div class="fold" style="left:387px"></div>
  <div class="fold" style="left:774px"></div>

  <div class="abs" style="left:28px;top:22px;width:335px">
    <h2 class="panel-title">ABOUT US</h2>
    <div class="rule"></div>
    <p class="body-copy body-copy--light" style="margin-top:10px">We are a full service cleaning company that offers a full range of quality cleaning services to fit your needs no matter the size. We offer commercial and residential cleaning services to fit any size property. We take pride in doing your dirty work. Clear Meadow Cleaning Services offers:</p>
    <ul class="service-list" style="margin-top:10px">
      <li><svg class="tick" viewBox="0 0 14 14"><circle cx="7" cy="7" r="7" fill="#fff"/><path d="M3.5 7.2l2.3 2.3 4.6-4.8" fill="none" stroke="var(--blue)" stroke-width="1.8"/></svg>Residential House Cleaning</li>
      <li><svg class="tick" viewBox="0 0 14 14"><circle cx="7" cy="7" r="7" fill="#fff"/><path d="M3.5 7.2l2.3 2.3 4.6-4.8" fill="none" stroke="var(--blue)" stroke-width="1.8"/></svg>Commercial Cleaning Services</li>
      <li><svg class="tick" viewBox="0 0 14 14"><circle cx="7" cy="7" r="7" fill="#fff"/><path d="M3.5 7.2l2.3 2.3 4.6-4.8" fill="none" stroke="var(--blue)" stroke-width="1.8"/></svg>Post Construction Cleaning</li>
      <li><svg class="tick" viewBox="0 0 14 14"><circle cx="7" cy="7" r="7" fill="#fff"/><path d="M3.5 7.2l2.3 2.3 4.6-4.8" fill="none" stroke="var(--blue)" stroke-width="1.8"/></svg>Move In &amp; Move Out Cleaning</li>
    </ul>
  </div>

  <div class="abs call-badge" style="left:540px;top:126px">
    <svg viewBox="0 0 24 24" width="16" height="16"><path d="M6.6 10.8a15 15 0 006.6 6.6l2.2-2.2a1 1 0 011-.25 11.4 11.4 0 003.6.57 1 1 0 011 1V20a1 1 0 01-1 1A17 17 0 013 4a1 1 0 011-1h3.5a1 1 0 011 1c0 1.25.2 2.45.57 3.57a1 1 0 01-.25 1z" fill="#fff"/></svg>
    <span style="margin-top:2px">CALL US<br>TODAY</span>
    <span>302-555-0148</span>
  </div>
  <div class="abs" style="left:410px;top:214px;width:340px">
    <h2 class="heading-green">Residential<br>Cleanings Services</h2>
    <p class="body-copy" style="margin-top:10px">Clear Meadow Cleaning Services residential cleaning service includes a thorough sweeping and vacuuming of all floors, dusting furniture, window sills, and washing all counters and appliances so they shine. Your house cleaners will meticulously clean every corner of your kitchen and bathrooms so they sparkle. You can always rely on Clear Meadow Cleaning Services for a remarkably detailed house cleaning.</p>
  </div>

  <h2 class="abs panel-title" style="left:800px;top:14px">COMMERCIAL CLEANING</h2>
  <div class="abs" style="left:800px;top:66px;width:340px">
    <p class="body-copy">Here at Clear Meadow Cleaning Services, we know that your offices are a direct reflection of your business. For years, we have helped businesses promote a more professional image by paying attention to every detail.</p>
    <p class="body-copy" style="margin-top:10px">Clear Meadow Cleaning Services offers a wide range of commercial cleaning services, such as:</p>
    <ul class="check-grid" style="margin-top:6px">
      <li><svg class="tick" viewBox="0 0 14 14"><circle cx="7" cy="7" r="7" fill="var(--green)"/><path d="M3.5 7.2l2.3 2.3 4.6-4.8" fill="none" stroke="#fff" stroke-width="1.8"/></svg>Office Cleaning</li>
      <li><svg class="tick" viewBox="0 0 14 14"><circle cx="7" cy="7" r="7" fill="var(--green)"/><path d="M3.5 7.2l2.3 2.3 4.6-4.8" fill="none" stroke="#fff" stroke-width="1.8"/></svg>Janitorial Services</li>
      <li><svg class="tick" viewBox="0 0 14 14"><circle cx="7" cy="7" r="7" fill="var(--green)"/><path d="M3.5 7.2l2.3 2.3 4.6-4.8" fill="none" stroke="#fff" stroke-width="1.8"/></svg>Floor Waxing</li>
      <li><svg class="tick" viewBox="0 0 14 14"><circle cx="7" cy="7" r="7" fill="var(--green)"/><path d="M3.5 7.2l2.3 2.3 4.6-4.8" fill="none" stroke="#fff" stroke-width="1.8"/></svg>Day Porter Services</li>
      <li><svg class="tick" viewBox="0 0 14 14"><circle cx="7" cy="7" r="7" fill="var(--green)"/><path d="M3.5 7.2l2.3 2.3 4.6-4.8" fill="none" stroke="#fff" stroke-width="1.8"/></svg>Window Cleaning</li>
      <li><svg class="tick" viewBox="0 0 14 14"><circle cx="7" cy="7" r="7" fill="var(--green)"/><path d="M3.5 7.2l2.3 2.3 4.6-4.8" fill="none" stroke="#fff" stroke-width="1.8"/></svg>Kitchen Cleaning</li>
      <li><svg class="tick" viewBox="0 0 14 14"><circle cx="7" cy="7" r="7" fill="var(--green)"/><path d="M3.5 7.2l2.3 2.3 4.6-4.8" fill="none" stroke="#fff" stroke-width="1.8"/></svg>Restroom Cleaning</li>
      <li><svg class="tick" viewBox="0 0 14 14"><circle cx="7" cy="7" r="7" fill="var(--green)"/><path d="M3.5 7.2l2.3 2.3 4.6-4.8" fill="none" stroke="#fff" stroke-width="1.8"/></svg>Construction Clean-up</li>
      <li><svg class="tick" viewBox="0 0 14 14"><circle cx="7" cy="7" r="7" fill="var(--green)"/><path d="M3.5 7.2l2.3 2.3 4.6-4.8" fill="none" stroke="#fff" stroke-width="1.8"/></svg>Deep Cleaning</li>
      <li><svg class="tick" viewBox="0 0 14 14"><circle cx="7" cy="7" r="7" fill="var(--green)"/><path d="M3.5 7.2l2.3 2.3 4.6-4.8" fill="none" stroke="#fff" stroke-width="1.8"/></svg>Vacant Buildings</li>
    </ul>
  </div>
  <p class="abs body-copy" style="left:800px;top:272px;width:190px">Whether you're looking for daily, weekly, bi-weekly or monthly cleaning for commercial properties, we will customize a schedule that works best for your customers and your employees.</p>
</section>

<section class="spread spread--outside" aria-label="Brochure outside">
  <svg class="backdrop" viewBox="0 0 1160 440" aria-hidden="true">
    <defs>
      <linearGradient id="photoLobby" x1="0" y1="0" x2="1" y2="1">
        <stop offset="0" stop-color="#f4f5f6"/><stop offset=".7" stop-color="#c3c7cb"/><stop offset="1" stop-color="#3a3d40"/>
      </linearGradient>
      <linearGradient id="photoTeam" x1="0" y1="0" x2="1" y2="1">
        <stop offset="0" stop-color="#efe9e1"/><stop offset=".55" stop-color="#9fb3bf"/><stop offset="1" stop-color="#e8cf55"/>
      </linearGradient>
    </defs>
    <rect x="0" y="0" width="387" height="440" fill="var(--blue)"/>
    <path d="M387 0C440 120 420 300 387 440H430C470 300 480 120 420 0Z" fill="var(--blue)"/>
    <path d="M420 0C480 120 470 300 430 440H452C495 300 505 120 446 0Z" fill="var(--green)"/>
    <circle cx="575" cy="108" r="98" fill="#fff"/>
    <circle cx="575" cy="108" r="92" fill="var(--mist)"/>
    <path d="M0 400C250 380 560 420 774 396V440H0Z" fill="var(--green)"/>
    <path d="M774 0H1160V90C1120 30 1040 0 970 0C900 0 830 30 774 90Z" fill="var(--blue)"/>
    <path d="M774 318C900 300 1040 300 1160 318V440H774Z" fill="var(--green)"/>
    <g role="img" aria-label="Photo: modern open office interior">
      <circle cx="112" cy="340" r="84" fill="var(--green)"/>
      <circle cx="112" cy="340" r="76" fill="url(#photoLobby)"/>
    </g>
    <g role="img" aria-label="Photo: cleaning team wiping a glass table">
      <circle cx="967" cy="96" r="92" fill="var(--green)"/>
      <circle cx="967" cy="96" r="84" fill="url(#photoTeam)"/>
    </g>
  </svg>
  <div class="fold" style="left:387px"></div>
  <div class="fold" style="left:774px"></div>

  <div class="abs" style="left:28px;top:22px;width:330px">
    <h2 class="panel-title">WHY CHOOSE US</h2>
    <div class="rule"></div>
    <ul class="why-list" style="margin-top:14px">
      <li><svg class="why-icon" viewBox="0 0 20 20"><circle cx="10" cy="10" r="9" fill="none" stroke="#fff" stroke-width="1.5"/><path d="M5.5 10.3l3 3 6-6.3" fill="none" stroke="#fff" stroke-width="1.8"/></svg>We Guarantee Our Work</li>
      <li><svg class="why-icon" viewBox="0 0 20 20"><circle cx="10" cy="10" r="9" fill="none" stroke="#fff" stroke-width="1.5"/><path d="M10 4.5v11M12.8 7.2c-.5-1-1.6-1.4-2.8-1.4-1.6 0-2.7.8-2.7 2s1 1.7 2.7 2.1 2.9 1 2.9 2.2-1.2 2.1-2.9 2.1c-1.3 0-2.4-.5-2.9-1.5" fill="none" stroke="#fff" stroke-width="1.4"/></svg>We're Affordable</li>
      <li><svg class="why-icon" viewBox="0 0 20 20"><circle cx="10" cy="10" r="9" fill="none" stroke="#fff" stroke-width="1.5"/><path d="M6 10h3v5H6zM9 10l2.5-4.5c1 0 1.5.7 1.3 1.7L12.3 9H15l-1 6H9" fill="none" stroke="#fff" stroke-width="1.3"/></svg>We're Thorough &amp; Reliable</li>
      <li><svg class="why-icon" viewBox="0 0 20 20"><circle cx="10" cy="10" r="9" fill="none" stroke="#fff" stroke-width="1.5"/><path d="M10 4.5l4.5 1.8v3.6c0 2.7-2 4.5-4.5 5.6-2.5-1.1-4.5-2.9-4.5-5.6V6.3z" fill="none" stroke="#fff" stroke-width="1.3"/></svg>Licensed and Insured<br>for your protection</li>
      <li><svg class="why-icon" viewBox="0 0 20 20"><circle cx="10" cy="10" r="9" fill="none" stroke="#fff" stroke-width="1.5"/><path d="M6 7h8M6 10h8M6 13h8" stroke="#fff" stroke-width="1.5"/></svg>We can design a cleaning<br>plan to fit your needs</li>
    </ul>
  </div>

  <div class="abs promise" style="left:487px;top:36px;width:176px">
    <div class="promise__cta">Contact<br>Us Today</div>
    <div class="promise__main" style="margin-top:4px">Satisfaction<br>Guaranteed!</div>
    <p class="promise__tag">It's not clean<br>unless it's<br>“Clear Meadow”<br>clean.</p>
  </div>
  <ul class="abs contact-list" style="left:520px;top:240px;width:250px">
    <li><svg class="contact-icon" viewBox="0 0 24 24"><path d="M6.6 10.8a15 15 0 006.6 6.6l2.2-2.2a1 1 0 011-.25 11.4 11.4 0 003.6.57 1 1 0 011 1V20a1 1 0 01-1 1A17 17 0 013 4a1 1 0 011-1h3.5a1 1 0 011 1c0 1.25.2 2.45.57 3.57a1 1 0 01-.25 1z" fill="none" stroke="var(--green)" stroke-width="1.6"/></svg>0400 555 019</li>
    <li><svg class="contact-icon" viewBox="0 0 24 24"><circle cx="12" cy="12" r="9.5" fill="none" stroke="var(--green)" stroke-width="1.6"/><path d="M2.5 12h19M12 2.5c3 3 3 16 0 19M12 2.5c-3 3-3 16 0 19" fill="none" stroke="var(--green)" stroke-width="1.4"/></svg>www.clearmeadowclean.example</li>
    <li><svg class="contact-icon" viewBox="0 0 24 24"><rect x="2.5" y="5" width="19" height="14" rx="1.5" fill="none" stroke="var(--green)" stroke-width="1.6"/><path d="M3 6l9 7 9-7" fill="none" stroke="var(--green)" stroke-width="1.6"/></svg>quentin@clearmeadowclean.example</li>
    <li><svg class="contact-icon" viewBox="0 0 24 24"><path d="M12 22s-7-7.2-7-12.2a7 7 0 0114 0C19 14.8 12 22 12 22z" fill="none" stroke="var(--green)" stroke-width="1.6"/><circle cx="12" cy="10" r="2.6" fill="none" stroke="var(--green)" stroke-width="1.6"/></svg>48 Birchwood Lane<br>Fairview, DE 19700</li>
  </ul>

  <div class="abs" style="left:790px;top:202px;width:355px">
    <p class="brand-name"><span class="brand-dot"></span>Clear Meadow Cleaning Services</p>
    <p class="brand-tag" style="margin-top:14px">We Enjoy Doing The Dirty work</p>
  </div>
  <div class="abs" style="left:774px;top:340px;width:386px">
    <p class="cover-band-title">Commercial and<br>Residential Cleaning</p>
    <p class="cover-url" style="margin-top:10px">www.clearmeadowclean.example</p>
  </div>
</section>

</body>
</html>
```